Microbrewery New 6-packs Design

We need a design for a microbrewery beer currently sold in single serve 500 mL bottles but that will now be sold in 6 packs. 6 bottles of 330 mL.

We need the graphic design that will be applied on the pannels of the beer pack. We are posting pictures of the 6-pack, however, we can customise its shape and design, so attention and ideas to that effect will enhance the graphic value of the project.

Target Market(s)

Microbrewery consumers. Higher end beer consumers willing to pay a premium for this type of product.

Requirements
Must have
• The consumer must be able to tell from the 6-pack that the product in it is the Dorrow IPA that he has been drinking in a 500 mL format.
Nice to have
• Small variation, die cuts, shapes to the design of the 6-pack so its stands out a bit vs. the competition

```html
<!DOCTYPE html>
<html lang="en">
<head>
<meta charset="utf-8">
<title>Dorrow IPA — 6-pack carrier panels</title>
<link rel="stylesheet" href="https://fonts.googleapis.com/css2?family=Amatic+SC:wght@700&family=Permanent+Marker&family=Special+Elite&display=swap">
<style>
  :root {
    --bg-light: #ffffff;
    --bg-edge: #d9d9d9;
    --pack-green: #0e4a30;
    --pack-green-dark: #0a3d27;
    --ink-white: #ecefe9;
    --ink-amber: #d8951f;
  }
  * { box-sizing: border-box; margin: 0; padding: 0; }
  html, body { width: 1200px; height: 1000px; overflow: hidden; }
  body {
    background: radial-gradient(ellipse at 50% 45%, var(--bg-light) 35%, var(--bg-edge) 100%);
    font-family: "Amatic SC", "Arial Narrow", sans-serif;
    position: relative;
  }
  .carrier {
    position: absolute;
    left: 285px;
    top: 335px;
    display: flex;
    gap: 0;
  }
  .panel {
    background: var(--pack-green);
    height: 475px;
    position: relative;
  }
  .panel--side {
    width: 185px;
    background: var(--pack-green-dark);
    border-right: 2px dashed rgba(255,255,255,0.15);
    display: flex;
    flex-direction: column;
    align-items: center;
    padding-top: 70px;
    color: var(--ink-white);
  }
  .panel--front {
    width: 440px;
  }
  .brand-name {
    font-family: "Amatic SC", "Arial Narrow", sans-serif;
    font-weight: 700;
    color: var(--ink-white);
    text-align: center;
    line-height: 0.9;
  }
  .panel--side .brand-name { font-size: 62px; }
  .tagline {
    font-family: "Amatic SC", "Arial Narrow", sans-serif;
    font-weight: 700;
    color: var(--ink-white);
    text-align: center;
    letter-spacing: 2px;
  }
  .panel--side .tagline { font-size: 30px; margin-top: 14px; }
  .ornament {
    width: 140px;
    height: 80px;
    margin-top: 16px;
    background: linear-gradient(180deg, rgba(216,149,31,0.55), rgba(216,149,31,0.25));
    border-radius: 4px;
  }
  .side-specs {
    margin-top: 14px;
    font-size: 26px;
    color: var(--ink-amber);
    letter-spacing: 2px;
  }
  .pack-count {
    position: absolute;
    left: 55px;
    top: 85px;
    font-family: "Special Elite", serif;
    font-size: 170px;
    color: var(--ink-white);
    line-height: 1;
  }
  .pack-word {
    position: absolute;
    left: 185px;
    top: 70px;
    font-family: "Permanent Marker", cursive;
    font-size: 68px;
    color: var(--ink-white);
    letter-spacing: 2px;
  }
  .pack-volume {
    position: absolute;
    left: 190px;
    top: 160px;
    font-family: "Special Elite", monospace;
    font-size: 50px;
    color: var(--ink-amber);
    letter-spacing: 6px;
  }
  .front-brand {
    position: absolute;
    left: 150px;
    top: 300px;
    width: 150px;
    display: flex;
    flex-direction: column;
    align-items: center;
  }
  .front-brand .brand-name { font-size: 52px; }
  .front-brand .tagline { font-size: 26px; margin-top: 8px; }
</style>
</head>
<body>
  <main class="carrier" aria-label="Dorrow IPA six-pack carrier panels">
    <section class="panel panel--side">
      <h1 class="brand-name">Dorrow<br>IPA</h1>
      <p class="tagline">India Pale Ale</p>
      <div class="ornament" role="img" aria-label="Hand-drawn sunburst and banner ornament in amber"></div>
      <p class="side-specs">500 ML · 6.5% ALC</p>
    </section>
    <section class="panel panel--front">
      <span class="pack-count">6</span>
      <span class="pack-word">PACK</span>
      <span class="pack-volume">500ML</span>
      <div class="front-brand">
        <h2 class="brand-name">Dorrow<br>IPA</h2>
        <p class="tagline">India Pale Ale</p>
      </div>
    </section>
  </main>
</body>
</html>
```